Product Insert / Thank You

I'm looking for a small card to be designed that will be included with our product when it ships. It will be 2 sided with 1 side being a "thank you" with our logo and the other side containing the following text:We would love to hear your feedback! For every review we receive on our products, we donate 100% of the proceeds of your order to TIDEWELL -- a non profit organization dedicated to preserving our oceans!If you are not 100% satisfied with your purchase or have any problems, we will always resolve your issue. please contact us via Brisko if you need assistance.Insert needs to be well organized and information presented in a clear and visually appealing way.
Target Market(s)
Women, aged 24-45
Colors
Designer to choose colors to be used in the design.
Look and feel
Each slider illustrates characteristics of the customer's brand and the style your logo design should communicate.

```html
<!DOCTYPE html>
<html lang="en">
<head>
<meta charset="utf-8">
<title>Ridgevale Thank You Insert</title>
<link href="https://fonts.googleapis.com/css2?family=Poiret+One&family=Lato:wght@400;700&display=swap" rel="stylesheet">
<style>
  :root {
    --canvas: #ffffff;
    --card-front: #ffffff;
    --sky: #f0eeea;
    --sea-light: #3a7d8f;
    --sea-deep: #1c5062;
    --ink: #111111;
    --rule: #2d5a6e;
    --shadow: rgba(0, 0, 0, 0.28);
  }
  * { margin: 0; padding: 0; box-sizing: border-box; }
  html, body {
    width: 1200px;
    height: 1200px;
    overflow: hidden;
    background: var(--canvas);
  }
  .canvas {
    position: relative;
    width: 1200px;
    height: 1200px;
  }
  .card {
    position: absolute;
    width: 776px;
    height: 516px;
    box-shadow: 4px 4px 6px var(--shadow);
    overflow: hidden;
  }
  .card--thanks {
    left: 58px;
    top: 118px;
    background: var(--sky);
  }
  .card--feedback {
    left: 363px;
    top: 580px;
    background: var(--card-front);
  }
  .sea-photo {
    position: absolute;
    left: 0;
    top: 268px;
    width: 100%;
    height: 248px;
    background: linear-gradient(180deg, var(--sea-light) 0%, #2c6a7d 45%, var(--sea-deep) 100%);
  }
  .brand {
    position: absolute;
    left: 0;
    top: 146px;
    width: 100%;
    display: flex;
    align-items: center;
    justify-content: center;
    gap: 10px;
    font-family: "Lato", sans-serif;
    font-weight: 700;
    font-size: 22px;
    letter-spacing: 2px;
    color: var(--ink);
  }
  .brand-dot {
    width: 18px;
    height: 18px;
    border: 2px solid var(--ink);
    border-radius: 50%;
  }
  .thanks-title {
    position: absolute;
    left: 0;
    top: 236px;
    width: 100%;
    text-align: center;
    font-family: "Poiret One", sans-serif;
    font-size: 58px;
    letter-spacing: 6px;
    color: var(--ink);
    padding-right: 30px;
  }
  .feedback-title {
    position: absolute;
    left: 0;
    top: 74px;
    width: 100%;
    text-align: center;
    font-family: "Poiret One", sans-serif;
    font-size: 43px;
    line-height: 47px;
    letter-spacing: 4px;
    color: var(--ink);
  }
  .feedback-rule {
    position: absolute;
    left: 289px;
    top: 213px;
    width: 198px;
    height: 2px;
    background: var(--rule);
  }
  .feedback-copy {
    position: absolute;
    left: 0;
    width: 100%;
    text-align: center;
    font-family: "Lato", sans-serif;
    font-size: 19.5px;
    line-height: 27.5px;
    color: var(--ink);
  }
  .feedback-copy--donation { top: 254px; }
  .feedback-copy--support { top: 364px; }
  .feedback-copy strong { font-weight: 700; }
</style>
</head>
<body>
<main class="canvas">
  <section class="card card--thanks">
    <div class="sea-photo" role="img" aria-label="Photograph of open blue ocean meeting a pale sky at the horizon"></div>
    <div class="brand"><span class="brand-dot"></span>RIDGEVALE</div>
    <h1 class="thanks-title">THANK YOU</h1>
  </section>

  <section class="card card--feedback">
    <h2 class="feedback-title">WE WOULD LOVE TO<br>HEAR YOUR FEEDBACK!</h2>
    <div class="feedback-rule"></div>
    <p class="feedback-copy feedback-copy--donation">
      For every review we receive on our products, we donate 100% of<br>
      the proceed of your order to “<strong>TIDEWELL</strong>” - a non profit<br>
      organization dedicated to preserving our oceans !
    </p>
    <p class="feedback-copy feedback-copy--support">
      If you’re not 100% satisfied with your purchase or have any<br>
      problems, we will always resolve your issue. Please contact us via<br>
      Brisko if you need assistance.
    </p>
  </section>
</main>
</body>
</html>
```